Velmar Industrial Coatings

We are looking to improve our business cards. Our company installs industrial floor and wall coatings in industrial, chemical and food processing plants.
Our coatings which consist of epoxy, urethane, and vinyl esters provide chemical and abrasion resistant surface with non-skid properties that are easy to clean.

Target Market(s)

food manufacturing, chemical plants, breweries and wineries, warehouses, clean room floors.

Industry/Entity Type

Construction

Contact Information for Business Card

improved current logo.

Colors

Designer to choose colors to be used in the design.

Requirements
Must have
• the information from uploaded file
Nice to have
• "We'll be outstanding on your floors."

```html
<!DOCTYPE html>
<html lang="en">
<head>
<meta charset="utf-8">
<title>Velmar Industrial Coatings — Business Cards</title>
<link href="https://fonts.googleapis.com/css2?family=Oswald:wght@300;600&family=Questrial&display=swap" rel="stylesheet">
<style>
  :root {
    --bg: #ece8e2;
    --sky: #8dd0f2;
    --sky-deep: #74c5ee;
    --navy: #152a4a;
    --teal: #0f7e9c;
    --teal-light: #1a91ad;
    --cyan: #22b8c8;
    --paper: #f5f5f5;
    --paper-shade: #e6e6e6;
    --ink: #3a3a3a;
    --white: #ffffff;
  }
  * { box-sizing: border-box; margin: 0; padding: 0; }
  html, body { width: 1200px; height: 456px; overflow: hidden; }
  body { background: var(--bg); font-family: "Questrial", sans-serif; position: relative; }

  .card {
    position: absolute;
    width: 350px;
    height: 200px;
    overflow: hidden;
    box-shadow: 0 4px 10px rgba(0,0,0,.18);
  }

  /* soft tonal areas where the pattern sits */
  .pattern-area { position: absolute; }
  .back-light .pattern-area { inset: 0; background: linear-gradient(135deg, var(--sky-deep) 0%, var(--sky) 45%, var(--sky) 60%, var(--sky-deep) 100%); }
  .back-navy .pattern-area { inset: 0; background: linear-gradient(135deg, #1b3459 0%, var(--navy) 45%, var(--navy) 60%, #1b3459 100%); }
  .front-white .pattern-area { left: 0; top: 0; width: 180px; height: 200px; background: linear-gradient(160deg, var(--paper-shade) 0%, var(--paper) 70%); }
  .front-teal .pattern-area { left: 0; top: 0; width: 180px; height: 200px; background: linear-gradient(160deg, #2a9fba 0%, var(--teal-light) 70%); }

  /* back sides */
  .back-light { left: 40px; top: 22px; background: var(--sky); }
  .back-navy  { left: 640px; top: 22px; background: var(--navy); }

  .badge {
    position: absolute;
    left: 133px; top: 48px;
    width: 86px; height: 86px;
    border-radius: 50%;
    background: var(--navy);
    border: 3px solid var(--cyan);
    display: flex; align-items: center; justify-content: center;
    font-size: 17px;
    letter-spacing: 1px;
    color: var(--cyan);
  }

  /* front sides */
  .front-white { left: 210px; top: 234px; background: var(--paper); }
  .front-teal  { left: 810px; top: 234px; background: var(--teal-light); }

  .logo-square {
    position: absolute;
    left: 34px; top: 44px;
    width: 76px; height: 58px;
    background: var(--navy);
    border: 2px solid var(--sky);
    display: flex; align-items: center; justify-content: center;
    font-size: 14px; letter-spacing: 1px;
    color: var(--sky);
  }
  .logo-circle {
    position: absolute;
    left: 30px; top: 30px;
    width: 92px; height: 92px;
    border-radius: 50%;
    background: var(--teal);
    border: 3px solid var(--cyan);
    display: flex; align-items: center; justify-content: center;
    font-size: 17px; letter-spacing: 1px;
    color: var(--navy);
  }

  .person { position: absolute; left: 30px; top: 128px; }
  .person-name { font-size: 13px; color: var(--teal); letter-spacing: .5px; white-space: nowrap; }
  .person-name b { font-weight: 700; }
  .person-name span { color: var(--ink); }
  .person-phone { font-family: "Oswald", sans-serif; font-weight: 300; font-size: 10px; color: var(--ink); margin-top: 1px; }
  .front-teal .person-name { color: #a8e4f4; }
  .front-teal .person-name span, .front-teal .person-phone { color: var(--navy); }

  .company { position: absolute; left: 190px; top: 18px; font-family: "Oswald", sans-serif; line-height: 1.05; }
  .company-top { font-weight: 300; font-size: 14px; color: var(--ink); }
  .company-main { font-weight: 600; font-size: 14.5px; color: var(--teal); white-space: nowrap; }
  .front-teal .company-top { color: var(--white); }
  .front-teal .company-main { color: #bfeaf6; }

  .info { position: absolute; left: 180px; top: 72px; width: 170px; color: var(--white); font-size: 9.5px; }
  .band { position: relative; background: var(--teal); padding-left: 20px; }
  .front-teal .band { background: var(--navy); }
  .band + .band { margin-top: 2px; }
  .band-address { height: 44px; padding-top: 3px; line-height: 1.2; }
  .band-address strong { font-weight: 700; display: block; }
  .band-phones { height: 42px; padding-top: 3px; line-height: 1.35; }
  .band-web { height: 18px; padding-top: 3px; }
  .row { position: relative; }
  .icon { position: absolute; width: 10px; height: 10px; }
  .band > .icon { left: 5px; top: 4px; }
  .row > .icon { left: -15px; top: 1px; }
</style>
</head>
<body>

  <!-- light variant -->
  <section class="card back-light" aria-label="Card back, light blue">
    <div class="pattern-area" role="img" aria-label="Soft light-blue background where faint rounded-square shapes sit"></div>
    <div class="badge">VELMAR</div>
  </section>

  <section class="card front-white" aria-label="Card front, white">
    <div class="pattern-area" role="img" aria-label="Light grey tile-grid floor pattern"></div>
    <div class="logo-square">VELMAR</div>
    <div class="person">
      <p class="person-name"><b>REED</b> <span>HALVORSEN</span></p>
      <p class="person-phone">1-800-555-0148</p>
    </div>
    <div class="company">
      <p class="company-top">VELMAR</p>
      <p class="company-main">INDUSTRIAL COATING INC.</p>
    </div>
    <div class="info">
      <div class="band band-address">
        <svg class="icon" viewBox="0 0 10 10" aria-hidden="true"><circle cx="5" cy="5" r="5" fill="var(--cyan)"/><circle cx="5" cy="4.3" r="1.6" fill="#fff"/></svg>
        <strong>Velmar Inc.</strong>PO.Box 412<br>Linden, WA 98540
      </div>
      <div class="band band-phones">
        <div class="row"><svg class="icon" viewBox="0 0 10 10" aria-hidden="true"><circle cx="5" cy="5" r="5" fill="var(--cyan)"/><rect x="2.5" y="4" width="5" height="3" fill="#fff"/></svg>(360) 555-0131</div>
        <div class="row"><svg class="icon" viewBox="0 0 10 10" aria-hidden="true"><circle cx="5" cy="5" r="5" fill="var(--cyan)"/><rect x="3" y="3" width="4" height="4" fill="#fff"/></svg>(360) 555-0133</div>
        <div class="row"><svg class="icon" viewBox="0 0 10 10" aria-hidden="true"><circle cx="5" cy="5" r="5" fill="var(--cyan)"/><path d="M3.5 2.5 L5 4 L4 5 Q5 6.5 6 6 L7 7 L6 7.8 Q3 7 2.5 3.5 Z" fill="#fff"/></svg>(360) 555-0176</div>
      </div>
      <div class="band band-web">
        <svg class="icon" viewBox="0 0 10 10" aria-hidden="true"><circle cx="5" cy="5" r="5" fill="var(--cyan)"/><path d="M3.5 2.5 L7 5 L5.3 5.3 L6.3 7.3 L5.6 7.6 L4.6 5.7 L3.5 6.8 Z" fill="#fff"/></svg>
        www.velmarfloors.com
      </div>
    </div>
  </section>

  <!-- dark variant -->
  <section class="card back-navy" aria-label="Card back, navy">
    <div class="pattern-area" role="img" aria-label="Soft navy background where cyan rounded-square shapes sit"></div>
    <div class="badge">VELMAR</div>
  </section>

  <section class="card front-teal" aria-label="Card front, teal">
    <div class="pattern-area" role="img" aria-label="Light teal tile-grid floor pattern"></div>
    <div class="logo-circle">VELMAR</div>
    <div class="person">
      <p class="person-name"><b>REED</b> <span>HALVORSEN</span></p>
      <p class="person-phone">1-800-555-0148</p>
    </div>
    <div class="company">
      <p class="company-top">VELMAR</p>
      <p class="company-main">INDUSTRIAL COATING INC.</p>
    </div>
    <div class="info">
      <div class="band band-address">
        <svg class="icon" viewBox="0 0 10 10" aria-hidden="true"><circle cx="5" cy="5" r="5" fill="var(--cyan)"/><circle cx="5" cy="4.3" r="1.6" fill="#fff"/></svg>
        <strong>Velmar Inc.</strong>PO.Box 412<br>Linden, WA 98540
      </div>
      <div class="band band-phones">
        <div class="row"><svg class="icon" viewBox="0 0 10 10" aria-hidden="true"><circle cx="5" cy="5" r="5" fill="var(--cyan)"/><rect x="2.5" y="4" width="5" height="3" fill="#fff"/></svg>(360) 555-0131</div>
        <div class="row"><svg class="icon" viewBox="0 0 10 10" aria-hidden="true"><circle cx="5" cy="5" r="5" fill="var(--cyan)"/><rect x="3" y="3" width="4" height="4" fill="#fff"/></svg>(360) 555-0133</div>
        <div class="row"><svg class="icon" viewBox="0 0 10 10" aria-hidden="true"><circle cx="5" cy="5" r="5" fill="var(--cyan)"/><path d="M3.5 2.5 L5 4 L4 5 Q5 6.5 6 6 L7 7 L6 7.8 Q3 7 2.5 3.5 Z" fill="#fff"/></svg>(360) 555-0176</div>
      </div>
      <div class="band band-web">
        <svg class="icon" viewBox="0 0 10 10" aria-hidden="true"><circle cx="5" cy="5" r="5" fill="var(--cyan)"/><path d="M3.5 2.5 L7 5 L5.3 5.3 L6.3 7.3 L5.6 7.6 L4.6 5.7 L3.5 6.8 Z" fill="#fff"/></svg>
        www.velmarfloors.com
      </div>
    </div>
  </section>

</body>
</html>
```